TIDEWELL PLUMBING

Just want to have ,sky blue logo, black back ground and I want incorporate the TIDEWELL part of my company name by having a person sliding and laying back looking like a rockstar with a tool or anything You think is cool doesn’t have to be that ,I’m open to anything ,I want you to use your imagination .
I want use it for my Vehicle and future business cards and other advertisement ventures.
PLUMBER -DRAINER,-GASFITTER/LPG

My number needs to be in there 0487153926

```html
<!DOCTYPE html>
<html lang="en">
<head>
<meta charset="utf-8">
<title>Tidewell Plumbing – Business Card</title>
<link rel="stylesheet" href="https://fonts.googleapis.com/css2?family=Michroma&family=Open+Sans:wght@700&display=swap">
<style>
  :root {
    --page: #ffffff;
    --card-black: #050505;
    --card-glow: #1e1e1e;
    --sky: #00b7ff;
    --white: #ffffff;
  }
  html, body {
    margin: 0;
    width: 1200px;
    height: 1200px;
    overflow: hidden;
    background: var(--page);
  }
  .canvas {
    position: relative;
    width: 1200px;
    height: 1200px;
  }
  .business-card {
    position: absolute;
    left: 105px;
    top: 309px;
    width: 1019px;
    height: 580px;
    display: block;
  }
  .wordmark {
    font-family: "Michroma", sans-serif;
    font-weight: 400;
    fill: var(--sky);
  }
  .phone-number {
    font-family: "Open Sans", sans-serif;
    font-weight: 700;
    fill: var(--white);
  }
  .services {
    font-family: "Open Sans", sans-serif;
    font-weight: 700;
    fill: var(--white);
    letter-spacing: 1px;
  }
</style>
</head>
<body>
<div class="canvas">
  <svg class="business-card" viewBox="0 0 1019 580" xmlns="http://www.w3.org/2000/svg">
    <defs>
      <radialGradient id="card-texture-tone" cx="50%" cy="42%" r="60%">
        <stop offset="0%" stop-color="var(--card-glow)"/>
        <stop offset="100%" stop-color="var(--card-black)"/>
      </radialGradient>
    </defs>

    <rect class="card-background" width="1019" height="580" fill="url(#card-texture-tone)"
          role="img" aria-label="Dark honeycomb mesh texture background"/>

    <!-- brand mark -->
    <circle class="brand-dot" cx="501" cy="182" r="58" fill="var(--sky)"/>
    <text class="wordmark brand-name" x="254" y="310" font-size="60" textLength="510" lengthAdjust="spacingAndGlyphs">TIDEWELL</text>
    <line class="rule rule-left" x1="255" y1="336" x2="385" y2="336" stroke="var(--sky)" stroke-width="2"/>
    <text class="wordmark brand-sub" x="395" y="347" font-size="26" textLength="228" lengthAdjust="spacingAndGlyphs">PLUMBING</text>
    <line class="rule rule-right" x1="633" y1="336" x2="764" y2="336" stroke="var(--sky)" stroke-width="2"/>

    <!-- contact -->
    <g class="phone-icon" fill="none" stroke="var(--sky)">
      <rect x="252" y="387" width="37" height="68" rx="6" stroke-width="5"/>
      <circle cx="270.5" cy="446" r="3" fill="var(--sky)" stroke="none"/>
      <line x1="265" y1="394" x2="276" y2="394" stroke-width="2.5"/>
    </g>
    <text class="phone-number" x="315" y="450" font-size="90" textLength="454" lengthAdjust="spacingAndGlyphs">0487153926</text>

    <!-- services band -->
    <rect class="services-band" x="0" y="491" width="1019" height="42" fill="var(--sky)"/>
    <text class="services" x="266" y="521" font-size="25" textLength="497" lengthAdjust="spacingAndGlyphs">PLUMBER  •  DRAINER • GASFITTER/LPG</text>
  </svg>
</div>
</body>
</html>
```